One Pager Fact Sheet Design

I need a couple of headers and footer designed to use for information security fact sheets to give to customers. Similar to the one listed below.

```html
<!DOCTYPE html>
<html lang="en">
<head>
<meta charset="utf-8">
<title>Netharbor – Fact Sheet Headers and Footer</title>
<link rel="stylesheet" href="https://fonts.googleapis.com/css2?family=Open+Sans:wght@400;600;700;800&display=swap">
<style>
  :root {
    --page-white: #ffffff;
    --panel-grey: #c9c3c4;
    --brand-red: #e3262b;
    --brand-red-deep: #d81f26;
    --brand-orange: #ee4a30;
    --glow-pink: #f27a92;
    --footer-bg: #f1eff0;
    --ink: #231f20;
    --social-blue: #2a8fd6;
  }
  * { box-sizing: border-box; margin: 0; padding: 0; }
  html, body {
    width: 1200px; height: 666px; overflow: hidden;
    background: var(--page-white);
    font-family: "Open Sans", Arial, sans-serif;
  }
  .canvas { position: relative; width: 1200px; height: 666px; }
  .sheet-panel {
    position: absolute; left: 58px; top: 44px; width: 1064px; height: 622px;
    background: var(--panel-grey);
  }
  .header-band {
    position: absolute; left: 68px; width: 1044px; overflow: hidden;
    background:
      linear-gradient(135deg, rgba(255,255,255,0) 0 30%, rgba(255,120,60,0.18) 30% 52%, rgba(255,255,255,0) 52%),
      linear-gradient(100deg, var(--brand-red-deep) 0%, var(--brand-red) 35%, var(--brand-orange) 60%, var(--brand-red) 100%);
  }
  .header-band--large { top: 84px; height: 223px; }
  .header-band--slim { top: 408px; height: 91px; }
  .security-visual {
    position: absolute; top: 0; right: 0; height: 100%;
    background: radial-gradient(ellipse at 55% 50%, rgba(248,160,180,0.75) 0%, rgba(242,122,146,0.45) 30%, rgba(238,74,48,0) 70%);
  }
  .header-band--large .security-visual { width: 520px; }
  .header-band--slim .security-visual { width: 340px; }
  .brand-lockup {
    position: absolute; display: flex; align-items: center;
    color: var(--page-white); font-weight: 800; letter-spacing: -0.5px;
  }
  .brand-mark {
    border-radius: 50%; border: solid var(--page-white); flex-shrink: 0;
  }
  .header-band--large .brand-lockup { left: 62px; top: 94px; font-size: 44px; gap: 12px; }
  .header-band--large .brand-mark { width: 62px; height: 62px; border-width: 7px; }
  .header-band--slim .brand-lockup { left: 40px; top: 26px; font-size: 28px; gap: 8px; }
  .header-band--slim .brand-mark { width: 38px; height: 38px; border-width: 4px; }

  .contact-footer {
    position: absolute; left: 68px; top: 558px; width: 1044px; height: 92px;
    background: var(--footer-bg); border-top: 5px solid var(--brand-red);
    display: flex; align-items: center; padding-left: 36px;
    font-size: 14px; color: var(--ink);
  }
  .contact-item { display: flex; align-items: center; gap: 6px; margin-right: 16px; white-space: nowrap; }
  .contact-icon {
    width: 20px; height: 20px; border-radius: 50%; background: var(--brand-red);
    display: flex; align-items: center; justify-content: center;
  }
  .contact-divider { width: 3px; height: 26px; background: var(--brand-red); margin: 0 14px 0 0; }
  .social-dots { display: flex; gap: 7px; margin-right: 8px; }
  .social-dot { width: 20px; height: 20px; border-radius: 50%; background: var(--social-blue); }
</style>
</head>
<body>
<div class="canvas">
  <div class="sheet-panel"></div>

  <header class="header-band header-band--large">
    <div class="security-visual" role="img" aria-label="Circuit board lines radiating from a shield emblem, in soft pink tones"></div>
    <div class="brand-lockup"><span class="brand-mark"></span><span class="brand-name">netharbor</span></div>
  </header>

  <header class="header-band header-band--slim">
    <div class="security-visual" role="img" aria-label="Circuit board lines around a shield emblem, in soft pink tones"></div>
    <div class="brand-lockup"><span class="brand-mark"></span><span class="brand-name">netharbor</span></div>
  </header>

  <footer class="contact-footer">
    <div class="contact-item">
      <span class="contact-icon">
        <svg width="12" height="12" viewBox="0 0 12 12" fill="none" stroke="#fff" stroke-width="1.2"><circle cx="6" cy="6" r="5"/><ellipse cx="6" cy="6" rx="2.2" ry="5"/><line x1="1" y1="6" x2="11" y2="6"/></svg>
      </span>
      <span>netharbor.example&nbsp; netharbor-info.example</span>
    </div>
    <div class="contact-item">
      <span class="contact-icon">
        <svg width="12" height="12" viewBox="0 0 12 12"><path d="M2 2 L11 5.5 L7 7 L5.5 11 Z" fill="#fff"/></svg>
      </span>
      <span>social.example/company/netharbor</span>
    </div>
    <div class="contact-item">
      <span class="contact-icon">
        <svg width="12" height="12" viewBox="0 0 12 12" fill="#fff"><path d="M1.5 4.5 Q6 1 10.5 4.5 L9.5 6 L8 5 L8 4 Q6 3.2 4 4 L4 5 L2.5 6 Z"/><rect x="3" y="6.5" width="6" height="3.5" rx="0.8"/></svg>
      </span>
      <span>01632 960 418</span>
    </div>
    <span class="contact-divider"></span>
    <div class="social-dots">
      <span class="social-dot"></span><span class="social-dot"></span><span class="social-dot"></span><span class="social-dot"></span>
    </div>
    <span>@netharbor.example</span>
  </footer>
</div>
</body>
</html>
```